Halcott Business Card Design

Photography business needs a logo. I would like to see creative licence on options on 1 & 2 sided. I really like the concept of a fully / partially frosted design. I have already used ArtisanHive for my Logo, so I am looking for the same level of assistance with this project.

Industry/Entity Type

Business

Font styles to use
Serif
Script

Requirements
Must have
• Must Have:
• - These are my contact details
• Name: Ames K Halcott
• Mobile: 5550193827
• email: lenorapaske@fernpost.net

```html
<!DOCTYPE html>
<html lang="en">
<head>
<meta charset="utf-8">
<title>Halcott Business Card Design</title>
<link href="https://fonts.googleapis.com/css2?family=Lato:wght@400;700&display=swap" rel="stylesheet">
<style>
  :root {
    --ink-deep: #0b0b0b;
    --ink-band: rgba(0, 0, 0, 0.5);
    --ink-band-strong: rgba(0, 0, 0, 0.82);
    --paper: #ffffff;
    --paper-soft: #e6e6e6;
    --accent-blue: #1565c0;
    --frame-line: #f2f2f2;
  }
  html, body {
    margin: 0;
    padding: 0;
    width: 1039px;
    height: 1200px;
    overflow: hidden;
    background: var(--paper);
    font-family: "Lato", sans-serif;
  }
  .sheet {
    position: relative;
    width: 1039px;
    height: 1200px;
    overflow: hidden;
  }

  /* Front card */
  .card-front {
    position: absolute;
    left: 0; top: 0;
    width: 1039px; height: 623px;
    background: var(--ink-deep);
    overflow: hidden;
  }
  .photo-panel { position: absolute; top: 0; height: 623px; }
  .photo-garden {
    left: 0; width: 358px;
    background:
      radial-gradient(ellipse 120px 260px at 200px 170px, rgba(235,235,235,0.95), rgba(235,235,235,0) 100%),
      linear-gradient(90deg, #2e2e2e 0%, #5c5c5c 14%, #9a9a9a 35%, #a8a8a8 60%, #4a4a4a 82%, #2a2a2a 100%),
      #5a5a5a;
    background-blend-mode: screen, normal, normal;
  }
  .photo-garden::after {
    content: "";
    position: absolute; inset: 0;
    background: linear-gradient(180deg, rgba(0,0,0,0) 0%, rgba(0,0,0,0) 45%, rgba(20,20,20,0.55) 75%, rgba(30,30,30,0.7) 100%);
  }
  .photo-photographer {
    left: 358px; width: 337px;
    background:
      radial-gradient(ellipse 260px 140px at 150px 210px, rgba(245,245,245,0.9), rgba(245,245,245,0) 100%),
      linear-gradient(180deg, #3c3c3c 0%, #7a7a7a 14%, #cfcfcf 32%, #9d9d9d 46%, #6a6a6a 58%, #2a2a2a 72%, #111 100%);
  }
  .photo-photographer::after {
    content: "";
    position: absolute; inset: 0;
    background: linear-gradient(90deg, rgba(0,0,0,0) 0%, rgba(0,0,0,0) 45%, rgba(0,0,0,0.55) 70%, rgba(0,0,0,0.75) 100%);
  }
  .photo-prints {
    left: 695px; width: 344px;
    background:
      radial-gradient(ellipse 220px 120px at 220px 330px, rgba(250,250,250,0.75), rgba(250,250,250,0) 100%),
      linear-gradient(180deg, #dedede 0%, #c8c8c8 28%, #9e9e9e 50%, #8a8a8a 70%, #6e6e6e 100%);
  }
  .info-band {
    position: absolute;
    left: 0; top: 393px;
    width: 1039px; height: 230px;
    background: var(--ink-band);
  }
  .info-band-center {
    position: absolute;
    left: 358px; top: 393px;
    width: 337px; height: 230px;
    background: var(--ink-band-strong);
  }
  .front-identity {
    position: absolute;
    left: 175px; top: 456px;
    width: 352px;
    color: var(--paper);
  }
  .front-name {
    display: block;
    font-size: 47px;
    font-weight: 700;
    line-height: 1;
    letter-spacing: -0.5px;
    text-align: right;
    background: linear-gradient(180deg, #ffffff 0%, #f0f0f0 50%, #b9b9b9 100%);
    -webkit-background-clip: text;
    background-clip: text;
    color: transparent;
    white-space: nowrap;
  }
  .front-role {
    display: block;
    margin-top: 10px;
    margin-left: 148px;
    font-size: 28px;
    line-height: 1;
  }
  .contact-list {
    position: absolute;
    left: 571px; top: 462px;
    margin: 0; padding: 0;
    list-style: none;
    color: var(--paper);
    font-size: 32px;
    font-weight: 700;
    line-height: 34px;
  }
  .contact-item { display: flex; align-items: center; gap: 14px; white-space: nowrap; }
  .contact-icon { width: 24px; height: 20px; flex: none; }

  /* Divider */
  .blue-band {
    position: absolute;
    left: 0; top: 623px;
    width: 1039px; height: 44px;
    background: var(--accent-blue);
  }

  /* Back card */
  .card-back {
    position: absolute;
    left: 0; top: 667px;
    width: 1039px; height: 533px;
    overflow: hidden;
  }
  .photo-camera-strap {
    position: absolute;
    left: 0; top: 0;
    width: 1039px; height: 533px;
    background:
      radial-gradient(ellipse 300px 200px at 150px 90px, rgba(250,250,250,0.7), rgba(250,250,250,0) 100%),
      radial-gradient(ellipse 420px 200px at 760px 140px, rgba(215,215,215,0.55), rgba(215,215,215,0) 100%),
      linear-gradient(90deg, #e2e2e2 0%, #d0d0d0 22%, #8e8e8e 34%, #7d7d7d 46%, #9c9c9c 60%, #8a8a8a 80%, #6f6f6f 100%);
  }
  .photo-camera-strap::after {
    content: "";
    position: absolute; inset: 0;
    background: linear-gradient(180deg, rgba(0,0,0,0) 0%, rgba(0,0,0,0) 55%, rgba(0,0,0,0.18) 100%);
  }
  .viewfinder { position: absolute; left: 0; top: 0; width: 1039px; height: 533px; }
  .back-identity {
    position: absolute;
    left: 428px; top: 212px;
    color: var(--paper);
  }
  .back-name {
    display: block;
    font-size: 74px;
    font-weight: 400;
    line-height: 1;
    letter-spacing: -1px;
    background: linear-gradient(180deg, #ffffff 0%, #f4f4f4 55%, #9a9a9a 100%);
    -webkit-background-clip: text;
    background-clip: text;
    color: transparent;
    white-space: nowrap;
  }
  .back-role {
    display: block;
    margin-top: -2px;
    margin-left: 124px;
    font-size: 32px;
    line-height: 1;
    text-shadow: 0 1px 3px rgba(0,0,0,0.35);
  }
</style>
</head>
<body>
<main class="sheet">
  <section class="card-front">
    <div class="photo-panel photo-garden" role="img" aria-label="Black and white photo of a woman in a gown walking toward a castle between tall hedges"></div>
    <div class="photo-panel photo-photographer" role="img" aria-label="Black and white silhouette of a photographer kneeling behind a camera on a tripod"></div>
    <div class="photo-panel photo-prints" role="img" aria-label="Black and white photo of an instant camera with scattered prints on a table"></div>
    <div class="info-band"></div>
    <div class="info-band-center"></div>
    <div class="front-identity">
      <span class="front-name">Ames K Halcott</span>
      <span class="front-role">Photographer</span>
    </div>
    <ul class="contact-list">
      <li class="contact-item">
        <svg class="contact-icon" viewBox="0 0 24 20" aria-hidden="true">
          <path d="M1 6 C4 1 20 1 23 6 L20 8 L17 6 L17 4 C14 3 10 3 7 4 L7 6 L4 8 Z" fill="#fff"/>
          <path d="M6 9 L18 9 L21 18 L3 18 Z" fill="#fff"/>
          <circle cx="12" cy="13" r="2.5" fill="#222"/>
        </svg>
        <span>5550193827</span>
      </li>
      <li class="contact-item">
        <svg class="contact-icon" viewBox="0 0 24 20" aria-hidden="true">
          <rect x="1" y="3" width="22" height="15" fill="none" stroke="#fff" stroke-width="2"/>
          <path d="M1 3 L12 12 L23 3 M1 18 L9 10 M23 18 L15 10" fill="none" stroke="#fff" stroke-width="2"/>
        </svg>
        <span>lenorapaske@fernpost.net</span>
      </li>
    </ul>
  </section>

  <div class="blue-band"></div>

  <section class="card-back">
    <div class="photo-camera-strap" role="img" aria-label="Soft-focus black and white photo of a film camera hanging from a strap beside a lace dress"></div>
    <svg class="viewfinder" viewBox="0 0 1039 533" aria-hidden="true">
      <g fill="none" stroke="var(--frame-line)" stroke-width="2.5">
        <path d="M71 141 L71 70 L142 70"/>
        <path d="M898 70 L968 70 L968 141"/>
        <path d="M71 483 L71 533"/>
        <path d="M968 483 L968 533"/>
      </g>
    </svg>
    <div class="back-identity">
      <span class="back-name">Ames K Halcott</span>
      <span class="back-role">Photographer</span>
    </div>
  </section>
</main>
</body>
</html>
```